Educate
Education
Creative Brief
It an educational site, N.G.O
Likes: Green White Green
above header
http://brevardlearning.org/
http://www.koltrex.org/offices/education/about/index.html

```html
<!DOCTYPE html>
<html lang="en">
<head>
<meta charset="utf-8">
<title>Education Centre</title>
<link rel="stylesheet" href="https://fonts.googleapis.com/css2?family=Arimo:wght@400;700&display=swap">
<style>
:root{
  --green:#13a02a;
  --green-dark:#0a7a1c;
  --green-light:#3cc94d;
  --green-text:#0f9a25;
  --yellow:#f1d21a;
  --yellow-light:#fbe96a;
  --grey-bg:#cfcfcf;
  --grey-band:#e4e4e4;
  --ink:#222;
  --white:#fff;
  --sky:#9fdcff;
}
*{margin:0;padding:0;box-sizing:border-box}
html,body{width:1200px;height:1054px;overflow:hidden}
body{background:var(--grey-bg);font-family:"Arimo",Arial,sans-serif;color:var(--ink);position:relative}
.page{position:absolute;left:34px;top:0;width:1132px;height:1054px;background:var(--white)}
.header{position:absolute;left:0;top:0;width:1132px;height:114px;background:linear-gradient(#2fc23f,var(--green) 60%,#0e8f22)}
.brand-mark{position:absolute;left:0;top:22px;width:72px;height:72px;border-radius:50%;background:#2a6fc4}
.brand-name{position:absolute;left:160px;top:32px;font-size:36px;font-weight:700;color:var(--white)}
.brand-tag{position:absolute;left:182px;top:70px;font-size:17px;font-weight:700;color:var(--sky)}
.nav{position:absolute;left:0;top:114px;width:1132px;height:46px;background:linear-gradient(#0d8d20,var(--green-dark));border-top:2px solid #5fd86b}
.nav a{position:absolute;top:12px;color:var(--white);font-size:20px;text-decoration:none;transform:translateX(-50%);white-space:nowrap}
.hero{position:absolute;left:0;top:163px;width:1132px;height:366px}
.promo{position:absolute;left:0;top:0;width:332px;height:180px;background:linear-gradient(var(--yellow-light),var(--yellow))}
.promo-icon{position:absolute;left:28px;top:48px}
.promo-title{position:absolute;left:120px;top:42px;font-size:34px;font-weight:700;color:var(--white);text-shadow:0 0 2px #b89a00}
.promo-sub{position:absolute;left:160px;top:96px;font-size:22px;color:var(--white)}
.courses{position:absolute;left:0;top:180px;width:332px;height:186px;background:linear-gradient(var(--green-light),var(--green))}
.courses h3{position:absolute;left:24px;top:10px;font-size:22px;color:var(--yellow-light);font-weight:700}
.courses-icon{position:absolute;left:28px;top:62px;width:56px;height:100px;background:linear-gradient(#e9e9e9,#555);border-radius:28px 28px 6px 6px}
.courses ul{position:absolute;left:100px;top:48px;list-style:none}
.courses li{color:var(--white);font-size:18px;height:40px;display:flex;align-items:center;gap:10px}
.tick{width:20px;height:20px;background:var(--white);display:flex;align-items:center;justify-content:center}
.hero-photo{position:absolute;left:332px;top:0;width:800px;height:366px;background:linear-gradient(100deg,#f4f4f4,#d9c4b3 40%,#b98f76 60%,#e9dcd2)}
.bands{position:absolute;left:0;top:535px;width:1132px;height:50px;background:linear-gradient(#f1f1f1,#d3d3d3)}
.bands h2{position:absolute;top:14px;font-size:20px;font-weight:400;transform:translateX(-50%);white-space:nowrap}
.content{position:absolute;left:0;top:585px;width:1132px;height:380px;background:var(--grey-band)}
.news{position:absolute;left:0;top:0;width:286px;height:380px;background:var(--white);padding:20px 14px}
.news-item{margin-bottom:16px}
.news-date{color:var(--green-text);font-size:14px;font-weight:700}
.news p,.about p{font-size:14px;line-height:18px}
.about{position:absolute;left:298px;top:0;width:540px;height:380px;background:var(--white);padding:14px 6px}
.about-photo{width:528px;height:136px;background:linear-gradient(90deg,#111,#333 60%,#777)}
.about p{margin-top:14px}
.areas{position:absolute;left:860px;top:0;width:272px;height:380px}
.area{position:absolute;left:6px;display:flex;gap:12px}
.area-photo{width:96px;height:76px;border:3px solid var(--white);box-shadow:0 0 3px #888}
.area p{color:var(--green-text);font-size:15px;font-weight:700;line-height:18px;width:150px}
.footer{position:absolute;left:0;top:966px;width:1132px;height:88px;background:linear-gradient(#3cc94d,var(--green) 50%,var(--green-dark))}
.copyright{position:absolute;left:24px;top:40px;font-size:15px;color:var(--yellow-light)}
.footer-nav{position:absolute;left:318px;top:36px;font-size:15px;color:var(--white);word-spacing:6px}
</style>
</head>
<body>
<div class="page">
  <header class="header">
    <div class="brand-mark"></div>
    <div class="brand-name">Education Centre</div>
    <div class="brand-tag">Best Education For You</div>
  </header>
  <nav class="nav">
    <a style="left:337px">Home</a><a style="left:426px">About Us</a><a style="left:531px">News</a><a style="left:640px">Educators</a><a style="left:763px">Families</a><a style="left:877px">Students</a><a style="left:991px">Contact</a>
  </nav>
  <section class="hero">
    <div class="promo">
      <svg class="promo-icon" width="80" height="60" viewBox="0 0 80 60"><polygon points="40,8 78,22 40,36 2,22" fill="#222"/><path d="M18 28v14c8 8 36 8 44 0V28L40 36z" fill="#333"/><line x1="70" y1="25" x2="70" y2="46" stroke="#d8a800" stroke-width="3"/></svg>
      <div class="promo-title">Competitive</div>
      <div class="promo-sub">examination</div>
    </div>
    <div class="courses">
      <h3>Our Programs &amp; Courses</h3>
      <div class="courses-icon" role="img" aria-label="Graduate figure icon"></div>
      <ul>
        <li><span class="tick"><svg width="14" height="14" viewBox="0 0 14 14"><path d="M2 7l3 3 7-7" stroke="#13a02a" stroke-width="2.5" fill="none"/></svg></span>Bilingual instructions</li>
        <li><span class="tick"><svg width="14" height="14" viewBox="0 0 14 14"><path d="M2 7l3 3 7-7" stroke="#13a02a" stroke-width="2.5" fill="none"/></svg></span>General education</li>
        <li><span class="tick"><svg width="14" height="14" viewBox="0 0 14 14"><path d="M2 7l3 3 7-7" stroke="#13a02a" stroke-width="2.5" fill="none"/></svg></span>Broad education</li>
      </ul>
    </div>
    <div class="hero-photo" role="img" aria-label="Group of smiling students holding books"></div>
  </section>
  <div class="bands">
    <h2 style="left:157px">Education News</h2>
    <h2 style="left:623px">About Education Program</h2>
    <h2 style="left:1000px">Education Program Areas</h2>
  </div>
  <main class="content">
    <div class="news">
      <div class="news-item"><div class="news-date">11.08.10</div><p>Lorem ipsum dolor sit amet, consectetur adipisicing elit, sed do eiusmod tempor incididunt ut labore et dolore magna aliqua.</p></div>
      <div class="news-item"><div class="news-date">11.08.10</div><p>Lorem ipsum dolor sit amet, consectetur adipisicing elit, sed do eiusmod tempor incididunt ut labore et dolore magna aliqua.</p></div>
      <div class="news-item"><div class="news-date">11.08.10</div><p>Lorem ipsum dolor sit amet, consectetur adipisicing elit, sed do eiusmod tempor incididunt ut labore et dolore magna aliqua.</p></div>
    </div>
    <div class="about">
      <div class="about-photo" role="img" aria-label="Hand writing formulas on a blackboard"></div>
      <p>Lorem ipsum dolor sit amet, consectetur adipisicing elit, sed do eiusmod tempor incididunt ut labore et dolore magna aliqua. Ut enim ad minim veniam, quis nostrud exercitation ullamco laboris nisi ut aliquip ex ea commodo consequat. Duis aute irure dolor in reprehenderit in voluptate velit esse cillum dolore eu fugiat nulla pariatur. Excepteur sint occaecat cupidatat non proident, sunt in culpa qui officia deserunt mollit anim id est laborum.</p>
    </div>
    <div class="areas">
      <div class="area" style="top:22px"><div class="area-photo" role="img" aria-label="Students in a classroom" style="background:linear-gradient(#c9b9a6,#6e5a48)"></div><p>Sed ut perspiciatis unde omnis iste natus error sit</p></div>
      <div class="area" style="top:120px"><div class="area-photo" role="img" aria-label="Teacher with a group of pupils" style="background:linear-gradient(#b8a58f,#5b4a3b)"></div><p>Sed ut perspiciatis unde omnis iste natus error sit</p></div>
      <div class="area" style="top:218px"><div class="area-photo" role="img" aria-label="Student studying at a desk" style="background:linear-gradient(#e2d7cc,#8d7766)"></div><p>Sed ut perspiciatis unde omnis iste natus error sit</p></div>
    </div>
  </main>
  <footer class="footer">
    <div class="copyright">Copyright@2010</div>
    <div class="footer-nav">Home &nbsp;| &nbsp;About Us &nbsp;| &nbsp;News &nbsp;| &nbsp;Educators &nbsp;| &nbsp;Families &nbsp;| &nbsp;Students &nbsp;| &nbsp;Contact</div>
  </footer>
</div>
</body>
</html>
```